Keystone Renewal
Cards and Stationary
Project: Keystone Renewal
Keystone Renewal - Environment
Creative Brief
Professional
Reid Hollister
Operations Manager
27 Marrow Lane Dunmere, Ov 10457
office@krflow.com
krflow.com
24/7 Emergency Water Removal Services
Pure Guild Certified in *Water Damage Restoration * Applied Structural Drying *Applied Microbial Remediation *Carpet Cleaning * Odor Control* Nrb Lead Safe Renovator * Level One Thermographer
Concepts
Business Cards, Letterhead, and Envelopes

```html
<!DOCTYPE html>
<html lang="en">
<head>
<meta charset="utf-8">
<title>Keystone Renewal – Cards and Stationery</title>
<link href="https://fonts.googleapis.com/css2?family=Open+Sans:wght@400;600;700&display=swap" rel="stylesheet">
<style>
:root{
  --board:#2a2b2d;
  --board-dark:#1c1d1f;
  --paper:#ffffff;
  --paper-shade:#e9edf1;
  --brand-blue:#1a6fb8;
  --brand-blue-dark:#0f4f8c;
  --brand-green:#3f8f2c;
  --ink:#3a3a3a;
  --ink-soft:#8a8f95;
  --label:#9a9da2;
  --mark-faint:rgba(26,111,184,0.10);
}
*{margin:0;padding:0;box-sizing:border-box}
html,body{width:1200px;height:422px;overflow:hidden}
body{
  background:radial-gradient(ellipse at center,var(--board) 0%,var(--board-dark) 100%);
  font-family:"Open Sans",Arial,sans-serif;
  position:relative;
}
.piece{position:absolute;background:var(--paper);box-shadow:0 3px 8px rgba(0,0,0,.55);overflow:hidden}
.label{position:absolute;font-size:5px;color:var(--label);text-align:center;letter-spacing:.2px}

.brand{display:flex;align-items:center;gap:3px;color:var(--brand-blue);font-weight:700;white-space:nowrap}
.brand .dot{border-radius:50%;background:var(--brand-blue);flex:none}

.watermark{position:absolute;display:flex;flex-direction:column;align-items:center;justify-content:center}
.watermark .ring{border-radius:50%;border:3px solid var(--mark-faint)}
.watermark .name{color:var(--mark-faint);font-weight:700;margin-top:5px;white-space:nowrap}

/* business cards */
.card{left:24px;width:150px;height:72px}
.card-front{top:106px}
.card-front .person{position:absolute;right:8px;top:7px;text-align:right;font-size:4.5px;color:var(--ink);line-height:1.4}
.card-front .person strong{font-size:5px}
.card-front .brand{position:absolute;left:8px;top:24px;font-size:8px}
.card-front .brand .dot{width:9px;height:9px}
.card-front .contact{position:absolute;left:8px;bottom:8px;font-size:4px;color:var(--ink-soft);line-height:1.45}
.card-front .edge{position:absolute;left:0;bottom:0;width:100%;height:3px;background:var(--brand-blue)}

.card-back{padding:8px 9px;font-size:4.3px;line-height:1.65}
.card-back ul{list-style:none}
.card-back li::before{content:"";display:inline-block;width:2.5px;height:2.5px;border-radius:50%;background:currentColor;margin-right:3px;vertical-align:middle}
.card-back .web{margin-top:3px;font-weight:700}
.card-back .watermark{right:10px;top:16px}
.card-back .watermark .ring{width:38px;height:38px}
.card-back.light{top:190px;color:var(--ink)}
.card-back.light .web{color:var(--brand-blue)}
.card-back.dark{top:274px;background:linear-gradient(135deg,var(--brand-blue) 0%,var(--brand-blue-dark) 100%);color:#fff}
.card-back.dark .watermark .ring{border-color:rgba(255,255,255,.15)}

/* letterheads */
.letterhead{top:28px;width:215px;height:310px;border-left:5px solid var(--brand-blue)}
.letterhead.one{left:250px}
.letterhead.two{left:478px}
.letterhead .brand{position:absolute;left:12px;top:12px;font-size:8px}
.letterhead .brand .dot{width:10px;height:10px}
.letterhead .head-contact{position:absolute;right:12px;top:12px;font-size:3.8px;color:var(--ink-soft);line-height:1.5;text-align:right}
.letterhead .watermark{left:0;right:0;top:95px}
.letterhead .watermark .ring{width:84px;height:84px}
.letterhead .watermark .name{font-size:8px}
.letterhead .foot{position:absolute;left:0;right:0;bottom:10px;font-size:3.8px;color:var(--ink-soft);text-align:center}

/* envelopes */
.envelope{height:78px}
.envelope .flap{position:absolute;inset:0;width:100%;height:100%}
.envelope .brand{position:absolute;left:12px;top:10px;font-size:7px}
.envelope .brand .dot{width:9px;height:9px}
.envelope .return{position:absolute;left:12px;top:24px;font-size:3.8px;color:var(--ink-soft);line-height:1.5}
.env-green{left:828px;top:30px;width:348px}
.env-blue{left:876px;top:96px;width:300px}
.env-plain{left:835px;top:172px;width:341px}
.env-front{left:828px;top:254px;width:336px;height:94px;border-left:5px solid var(--brand-blue)}
.env-front .watermark{left:0;right:0;top:14px}
.env-front .watermark .ring{width:60px;height:60px}
</style>
</head>
<body>

<div class="piece card card-front">
  <div class="person"><strong>Reid Hollister</strong><br>Operations Manager</div>
  <div class="brand"><span class="dot"></span>Keystone Renewal</div>
  <div class="contact">27 Marrow Lane Dunmere, Ov 10457<br>office@krflow.com<br>krflow.com</div>
  <div class="edge"></div>
</div>
<div class="label" style="left:24px;top:181px;width:150px">Front Side</div>

<div class="piece card card-back light">
  <ul>
    <li>Water Damage Restoration</li>
    <li>Structural Drying</li>
    <li>Microbial Remediation</li>
    <li>Carpet Cleaning</li>
    <li>Odor Control</li>
  </ul>
  <div class="web">krflow.com</div>
  <div class="watermark"><div class="ring"></div></div>
</div>
<div class="label" style="left:24px;top:265px;width:150px">Back Side Option 1</div>

<div class="piece card card-back dark">
  <ul>
    <li>Water Damage Restoration</li>
    <li>Structural Drying</li>
    <li>Microbial Remediation</li>
    <li>Carpet Cleaning</li>
    <li>Odor Control</li>
  </ul>
  <div class="web">krflow.com</div>
  <div class="watermark"><div class="ring"></div></div>
</div>
<div class="label" style="left:24px;top:350px;width:150px">Back Side Option 2</div>

<div class="piece letterhead one">
  <div class="brand"><span class="dot"></span>Keystone Renewal</div>
  <div class="head-contact">27 Marrow Lane<br>Dunmere, Ov 10457<br>office@krflow.com<br>krflow.com</div>
  <div class="watermark"><div class="ring"></div><div class="name">Keystone Renewal</div></div>
  <div class="foot">krflow.com</div>
</div>
<div class="label" style="left:250px;top:344px;width:215px">Letterhead Layout 1</div>

<div class="piece letterhead two">
  <div class="brand"><span class="dot"></span>Keystone Renewal</div>
  <div class="watermark"><div class="ring"></div><div class="name">Keystone Renewal</div></div>
  <div class="foot">27 Marrow Lane Dunmere, Ov 10457 · office@krflow.com · krflow.com</div>
</div>
<div class="label" style="left:478px;top:344px;width:215px">Letterhead Layout 2</div>

<div class="piece envelope env-green">
  <svg class="flap" viewBox="0 0 348 78" preserveAspectRatio="none"><polygon points="0,0 348,0 348,40 174,70 0,40" fill="var(--brand-green)"/></svg>
</div>
<div class="piece envelope env-blue">
  <svg class="flap" viewBox="0 0 300 78" preserveAspectRatio="none"><polygon points="0,0 300,0 300,38 150,68 0,38" fill="var(--brand-blue)"/></svg>
</div>
<div class="piece envelope env-plain">
  <svg class="flap" viewBox="0 0 341 78" preserveAspectRatio="none"><polyline points="0,30 170,64 341,30" fill="none" stroke="var(--paper-shade)" stroke-width="2"/></svg>
</div>
<div class="piece envelope env-front">
  <div class="brand"><span class="dot"></span>Keystone Renewal</div>
  <div class="return">27 Marrow Lane<br>Dunmere, Ov 10457</div>
  <div class="watermark"><div class="ring"></div></div>
</div>
<div class="label" style="left:828px;top:356px;width:348px">Envelope Layout</div>

</body>
</html>
```